Business software developers new website

We need to redesign our website. Our current website is http://www.plumvista.net/index.html, which is outdated and needs a new look. We moved out from web design and have concentrated more on the back end of the systems, for example, system support and security and cloud-based applications. Our major clients include both private and government sectors. We would like to see some designs that are all in one page, simple and clean. Prefer illustrator or obstructed images instead of real-life photos. Must look futuristic yet friendly. Attached the new logo for your references and good luck.

Target Market(s)

Medium to big company for their IT or data management. Either improve or upgrade their current system.

Industry/Entity Type

Business Software

Number of Pages Required

1 page

Colors

Designer to choose colors to be used in the design.

Requirements
Must have
• Simple and clean. Individual assets must be provided in the correct size and format(png or jpeg). Prefer Goggle fonts. Even though the logo color is red, grey and black, still prefer some modern colors that go well with red. When design, must consider the possibility to convert it into responsive.
Nice to have
• White background
Should not have
• real life photos, no slider

```html
<!DOCTYPE html>
<html lang="en">
<head>
<meta charset="utf-8">
<title>Plumvista.net — System Support, Security and Cloud</title>
<link href="https://fonts.googleapis.com/css2?family=Jost:wght@300;400;500&family=Roboto+Condensed:wght@300;400;700&display=swap" rel="stylesheet">
<style>
:root{
  --red:#e3323b;
  --ink:#2b2b2b;
  --text:#555;
  --muted:#8a8a8a;
  --line:#e2e2e2;
  --soft:#f5f5f5;
  --navy:#2a1a8c;
  --navy-deep:#1c1266;
  --teal:#1fc7c1;
  --footer:#2b2b2b;
}
*{box-sizing:border-box;margin:0;padding:0}
html,body{width:1200px;height:4096px;overflow:hidden}
body{position:relative;background:#fff;font-family:"Jost",sans-serif;color:var(--text)}
.abs{position:absolute}
.band{position:absolute;left:0;width:1200px}
.h-title{font-family:"Roboto Condensed",sans-serif;font-weight:700;font-size:31px;color:var(--ink);line-height:1}
.h-title span{color:var(--red)}
.mark{position:absolute;display:flex;align-items:center;gap:8px}
.mark i{display:block;width:16px;height:16px;border-radius:50%;background:var(--red)}
.mark b{display:block;height:1px;background:var(--line)}
.btn{position:absolute;display:flex;align-items:center;gap:10px;height:33px;padding:0 16px 0 7px;background:var(--red);color:#fff;border-radius:4px 16px 16px 4px;font-size:13px;font-weight:500;white-space:nowrap}
.btn i{display:block;width:22px;height:22px;border-radius:50%;background:#fff}
.para{position:absolute;font-size:13px;line-height:25.5px;text-align:justify;color:var(--text)}
.arrow{position:absolute;width:32px;height:32px;border-radius:50%;background:#fff;box-shadow:0 2px 8px rgba(0,0,0,.15);display:flex;align-items:center;justify-content:center}
.social{display:block;width:22px;height:22px;border-radius:50%;background:var(--red)}

/* top bar & nav */
.topbar{top:0;height:45px;background:#fff;font-size:13px;color:var(--ink)}
.topbar .item{position:absolute;top:13px;display:flex;align-items:center;gap:8px}
.topbar .socials{position:absolute;top:11px;left:973px;display:flex;gap:8px}
.nav{top:45px;height:82px;background:var(--soft);border-bottom:1px solid var(--line)}
.brand{position:absolute;font-family:"Jost",sans-serif;font-weight:400;color:var(--ink);letter-spacing:.5px}
.nav .brand{left:141px;top:20px;font-size:38px}
.menu{position:absolute;top:33px;left:740px;display:flex;gap:30px;font-size:13px;color:var(--ink)}
.menu .active{color:var(--red);position:relative;font-weight:500}
.menu .active:before{content:"";position:absolute;left:50%;top:-20px;width:14px;height:14px;margin-left:-7px;border-radius:50%;background:#f4b9bc}

/* hero */
.hero{top:127px;height:458px;background:linear-gradient(135deg,var(--navy) 0%,var(--navy-deep) 100%)}
.hero .l1{left:141px;top:120px;font-family:"Roboto Condensed",sans-serif;font-weight:300;font-size:35px;color:#fff}
.hero .l2{left:141px;top:162px;font-family:"Roboto Condensed",sans-serif;font-weight:700;font-size:35px;color:#fff}
.hero .l3{left:141px;top:206px;font-family:"Roboto Condensed",sans-serif;font-weight:700;font-size:24px;color:#fff}
.hero-art{left:620px;top:48px;width:350px;height:358px;border-radius:40%;background:radial-gradient(circle,#2fe0d6 0%,#18a9b4 45%,rgba(42,26,140,0) 72%)}

/* about */
.about{top:585px;height:565px;background:var(--soft)}
.about-art{left:142px;top:70px;width:422px;height:422px;border-radius:50%;border:1px dashed #e89aa0;display:flex;align-items:center;justify-content:center}
.about-art div{width:360px;height:360px;border-radius:50%;background:radial-gradient(circle,#cfe8f6 0%,#e6f3fa 70%,#f1f8fc 100%)}

/* clients */
.clients{top:1150px;height:586px;background:#fff}
.logo-card{position:absolute;background:#fff;box-shadow:0 2px 10px rgba(0,0,0,.1);display:flex;align-items:center;justify-content:center;font-family:"Roboto Condensed",sans-serif;font-weight:700;font-size:17px;color:#333;letter-spacing:1px}

/* services */
.services{top:1736px;height:439px;background:var(--soft)}
.svc{position:absolute;top:161px;width:190px;margin-left:-95px;text-align:center}
.svc .disc{width:142px;height:142px;margin:0 auto;border-radius:50%;background:#fff;box-shadow:0 4px 14px rgba(0,0,0,.12);display:flex;align-items:center;justify-content:center}
.svc.on .disc{border:4px solid var(--red)}
.svc p{margin-top:22px;font-size:16px;line-height:21px;color:var(--ink);font-weight:500}

/* news */
.news{top:2175px;height:623px;background:#fff}
.card{position:absolute;top:157px;width:286px;height:393px;border:1px solid #ddd;background:#fff}
.card .pic{position:absolute;left:7px;top:7px;width:270px;height:168px}
.card .date{position:absolute;right:7px;top:7px;width:36px;height:38px;background:var(--red);color:#fff;text-align:center;font-size:17px;font-weight:500;line-height:20px;padding-top:2px}
.card .date small{display:block;font-size:8px;line-height:10px}
.card h3{position:absolute;left:15px;top:195px;width:255px;font-size:15.5px;font-weight:500;line-height:21px;color:var(--ink)}
.card p{position:absolute;left:15px;top:248px;width:240px;font-size:12.5px;line-height:23px;color:var(--text)}
.card .btn{left:15px;top:334px;height:31px}

/* faq & philosophy */
.faq{top:2798px;height:462px;background:var(--soft)}
.acc-open{left:141px;top:169px;width:424px;height:41px;background:var(--red);color:#fff;font-size:12.5px;display:flex;align-items:center;justify-content:space-between;padding:0 15px}
.acc-body{left:141px;top:210px;width:424px;padding:10px 8px 0 15px;font-size:12.5px;line-height:23px;color:var(--text);border-left:1px solid #ddd;border-right:1px solid #ddd;height:118px}
.acc-closed{left:141px;top:345px;width:424px;height:40px;background:#fff;border:1px solid #ddd;font-size:12.5px;color:var(--ink);display:flex;align-items:center;justify-content:space-between;padding:0 15px}
.acc-closed b{color:var(--red);font-size:18px;font-weight:400}
.divider{left:600px;top:56px;height:358px;border-left:1px dashed #d2a2a5}
.philo{left:636px;top:167px;width:423px;height:220px;background:#fff;box-shadow:0 4px 20px rgba(0,0,0,.08)}

/* contact */
.contact{top:3260px;height:532px;background:#fff}
.field{position:absolute;border:1px solid #ddd;background:#fff;font-size:11.5px;color:#777;padding:10px 14px}
.robot{display:flex;align-items:center;gap:12px;padding:0 12px}
.robot i{display:block;width:20px;height:20px;border:1px solid #bbb;border-radius:2px}
.robot em{margin-left:auto;width:20px;height:20px;border-radius:50%;background:#c7d3ee;font-style:normal}

/* footer */
.footer{top:3792px;height:304px;background:var(--footer);color:#cfcfcf}
.footer .brand{left:141px;top:68px;font-size:30px;color:#fff}
.f-text{position:absolute;font-size:12px;line-height:21px;color:#cfcfcf}
.f-head{position:absolute;top:72px;font-size:14px;font-weight:500;color:#fff;letter-spacing:.5px;text-transform:uppercase}
.f-head span{color:var(--red)}
.f-head:after{content:"";position:absolute;left:0;top:24px;width:36px;height:2px;background:var(--red)}
.f-list{position:absolute;top:112px;font-size:12px;list-style:none}
.f-list li{display:flex;align-items:center;gap:10px;height:29px}
.f-links li{height:26px}
.sub-form{left:776px;top:138px;width:284px;height:29px;background:#fff;border-radius:15px;display:flex;overflow:hidden}
.sub-form span{flex:1;font-size:11.5px;color:#888;padding:7px 14px}
.sub-form b{width:81px;background:var(--red);color:#fff;font-size:13px;font-weight:500;display:flex;align-items:center;justify-content:center;border-radius:15px}
.f-rule{left:0;top:246px;width:1200px;height:1px;background:#444}
.copy{left:0;top:267px;width:1200px;text-align:center;font-size:12px;color:#cfcfcf}
</style>
</head>
<body>

<!-- Top bar -->
<header class="band topbar">
  <div class="item" style="left:141px">
    <svg width="16" height="16" viewBox="0 0 24 24" fill="none" stroke="#e3323b" stroke-width="2"><path d="M5 3h4l2 5-2.5 1.5a11 11 0 0 0 6 6L16 13l5 2v4a2 2 0 0 1-2 2A16 16 0 0 1 3 5a2 2 0 0 1 2-2z"/></svg>
    +61 7 5550 1234
  </div>
  <div class="item" style="left:300px">
    <svg width="18" height="14" viewBox="0 0 24 18" fill="none" stroke="#e3323b" stroke-width="2"><rect x="1" y="1" width="22" height="16" rx="1"/><path d="M1 2l11 8 11-8"/></svg>
    info@plumvista.com
  </div>
  <div class="socials" aria-label="Social links">
    <i class="social"></i><i class="social"></i><i class="social"></i>
  </div>
</header>

<nav class="band nav">
  <div class="brand">plumvista•net</div>
  <div class="menu">
    <span class="active">Home</span>
    <span>Our Services</span>
    <span>Our Clients</span>
    <span>Contact Us</span>
  </div>
</nav>

<!-- Hero -->
<section class="band hero">
  <div class="abs l1">We provide best quality</div>
  <div class="abs l2">Service for System Support,</div>
  <div class="abs l3">Security and Cloud-based applications</div>
  <div class="btn" style="left:141px;top:267px"><i></i>Let's Get Started</div>
  <div class="abs hero-art" role="img" aria-label="Isometric illustration of a businessman standing on a glowing server platform surrounded by data panels"></div>
</section>

<!-- About -->
<section class="band about">
  <div class="abs about-art"><div role="img" aria-label="Illustration of a team on a video call around a laptop"></div></div>
  <h2 class="abs h-title" style="left:653px;top:136px">ABOUT <span>US</span></h2>
  <div class="mark" style="left:653px;top:178px"><i></i><b style="width:90px"></b></div>
  <p class="para" style="left:653px;top:216px;width:406px">We have provided web design, graphic design and application development solutions for a wide variety of industries. We are known for the quality of our work, affordable rates and our individual approach to each customer. Our company offers a wide variety of professional web solution and all this at very competitive prices!</p>
  <div class="btn" style="left:657px;top:393px"><i></i>Read More</div>
</section>

<!-- Clients -->
<section class="band clients">
  <h2 class="abs h-title" style="left:141px;top:170px">Our <span>Clients</span></h2>
  <div class="mark" style="left:141px;top:212px"><i></i><b style="width:110px"></b></div>
  <p class="para" style="left:141px;top:250px;width:402px">We undertake many projects from small businesses to large corporations. We are also extremely experienced in the long term support of comprehensive web based business systems providing first class development, maintenance, data entry services and enhancements. Click here to see more details.</p>
  <div class="btn" style="left:141px;top:400px"><i></i>Read More</div>
  <div class="arrow" style="left:599px;top:313px"><svg width="8" height="10" viewBox="0 0 8 10"><path d="M6 0L0 5l6 5z" fill="#999"/></svg></div>
  <div class="arrow" style="left:1054px;top:313px"><svg width="8" height="10" viewBox="0 0 8 10"><path d="M2 0l6 5-6 5z" fill="#999"/></svg></div>
  <div class="logo-card" style="left:680px;top:201px;width:155px;height:99px">HARLOW STUDIO</div>
  <div class="logo-card" style="left:849px;top:220px;width:154px;height:99px">NORTHGATE</div>
  <div class="logo-card" style="left:680px;top:314px;width:155px;height:99px">WALDEN CO</div>
  <div class="logo-card" style="left:849px;top:335px;width:154px;height:99px">EAGLE ROW</div>
</section>

<!-- Services -->
<section class="band services">
  <h2 class="abs h-title" style="left:0;width:1200px;text-align:center;top:74px">Our <span>Services</span></h2>
  <div class="mark" style="left:520px;top:115px"><b style="width:72px"></b><i></i><b style="width:72px"></b></div>
  <div class="arrow" style="left:76px;top:219px"><svg width="8" height="10" viewBox="0 0 8 10"><path d="M6 0L0 5l6 5z" fill="#999"/></svg></div>
  <div class="arrow" style="left:1092px;top:219px"><svg width="8" height="10" viewBox="0 0 8 10"><path d="M2 0l6 5-6 5z" fill="#999"/></svg></div>

  <div class="svc" style="left:213px"><div class="disc">
    <svg width="66" height="70" viewBox="0 0 66 70" fill="none" stroke-width="2.5"><path d="M33 4l25 9v20c0 16-11 27-25 33C19 60 8 49 8 33V13z" stroke="#3a3a6a"/><path d="M33 13l17 6v14c0 11-7 19-17 23-10-4-17-12-17-23V19z" fill="#f7c9cc" stroke="#e3323b"/><path d="M24 34l7 7 12-13" stroke="#3a3a6a"/></svg>
  </div><p>Security &amp; Firewalls</p></div>

  <div class="svc" style="left:407px"><div class="disc">
    <svg width="76" height="62" viewBox="0 0 76 62" fill="none" stroke="#3a3a6a" stroke-width="2.5"><rect x="3" y="4" width="46" height="34" rx="2"/><path d="M18 52h18M27 38v14"/><rect x="52" y="16" width="20" height="42" rx="2" fill="#f7c9cc" stroke="#e3323b"/><path d="M57 24h10M57 31h10" stroke="#e3323b"/></svg>
  </div><p>Workstation<br>Support</p></div>

  <div class="svc on" style="left:599px"><div class="disc">
    <svg width="56" height="66" viewBox="0 0 56 66" fill="none" stroke="#3a3a6a" stroke-width="2.5"><rect x="3" y="3" width="50" height="60" rx="4"/><rect x="10" y="11" width="36" height="10" rx="2" fill="#f7c9cc" stroke="#e3323b"/><rect x="10" y="28" width="36" height="10" rx="2"/><rect x="10" y="45" width="36" height="10" rx="2"/></svg>
  </div><p>Storage</p></div>

  <div class="svc" style="left:793px"><div class="disc">
    <svg width="74" height="66" viewBox="0 0 74 66" fill="none" stroke="#3a3a6a" stroke-width="2.5"><path d="M18 40a12 12 0 0 1 2-24 17 17 0 0 1 32 2 11 11 0 0 1 4 22"/><rect x="27" y="22" width="20" height="40" rx="2" fill="#f7c9cc" stroke="#e3323b"/><path d="M32 30h10M32 37h10" stroke="#e3323b"/></svg>
  </div><p>Networks &amp;<br>Databases</p></div>

  <div class="svc" style="left:987px"><div class="disc">
    <svg width="76" height="66" viewBox="0 0 76 66" fill="none" stroke="#3a3a6a" stroke-width="2.5"><path d="M18 38a13 13 0 0 1 2-26 19 19 0 0 1 36 2 12 12 0 0 1 2 24z"/><path d="M26 38v12M38 38v16M50 38v12"/><circle cx="26" cy="54" r="3.5" fill="#f7c9cc" stroke="#e3323b"/><circle cx="38" cy="58" r="3.5" fill="#f7c9cc" stroke="#e3323b"/><circle cx="50" cy="54" r="3.5" fill="#f7c9cc" stroke="#e3323b"/></svg>
  </div><p>Cloud</p></div>
</section>

<!-- News -->
<section class="band news">
  <h2 class="abs h-title" style="left:0;width:1200px;text-align:center;top:71px">Latest <span>News</span></h2>
  <div class="mark" style="left:520px;top:112px"><b style="width:72px"></b><i></i><b style="width:72px"></b></div>
  <div class="arrow" style="left:76px;top:351px"><svg width="8" height="10" viewBox="0 0 8 10"><path d="M6 0L0 5l6 5z" fill="#999"/></svg></div>
  <div class="arrow" style="left:1092px;top:351px"><svg width="8" height="10" viewBox="0 0 8 10"><path d="M2 0l6 5-6 5z" fill="#999"/></svg></div>

  <article class="card" style="left:141px">
    <div class="pic" role="img" aria-label="Glowing digital globe above a city at night" style="background:linear-gradient(160deg,#0f3a4e,#1d7c96 55%,#0b1e2c)"></div>
    <div class="date">21<small>NOV</small></div>
    <h3>Website: Plumvista.net launches new website.</h3>
    <p>Our work is based on quality sales, customer and technical support services.</p>
    <div class="btn"><i></i>Read More</div>
  </article>
  <article class="card" style="left:456px">
    <div class="pic" role="img" aria-label="Padlock on a glowing computer screen" style="background:linear-gradient(160deg,#1a2c7a,#c8354a 55%,#2a3aa8)"></div>
    <div class="date">21<small>NOV</small></div>
    <h3>Website: Plumvista.net launches new website.</h3>
    <p>Our work is based on quality sales, customer and technical support services.</p>
    <div class="btn"><i></i>Read More</div>
  </article>
  <article class="card" style="left:771px">
    <div class="pic" role="img" aria-label="Businessman touching a virtual chart interface" style="background:linear-gradient(160deg,#c9d6e6,#7d96b4 55%,#1f2b3d)"></div>
    <div class="date">21<small>NOV</small></div>
    <h3>Website: Plumvista.net launches new website.</h3>
    <p>Our work is based on quality sales, customer and technical support services.</p>
    <div class="btn"><i></i>Read More</div>
  </article>
</section>

<!-- FAQ & Philosophy -->
<section class="band faq">
  <h2 class="abs h-title" style="left:141px;top:72px">Frequently <span>Asked Questions</span></h2>
  <div class="mark" style="left:141px;top:114px"><i></i></div>
  <div class="abs acc-open"><span>How much does a web site powered by Plumvista.net cost?</span><span>–</span></div>
  <div class="abs acc-body">There are quite a few factors that are going to affect the ultimate cost of your web site. These factors include how many pages you are going to have, if you will sell products on your website, the graphic work involved, and how interactive your web site will be.</div>
  <div class="abs acc-closed"><span>How long does it take to have a web site designed?</span><b>+</b></div>

  <div class="abs divider"></div>

  <h2 class="abs h-title" style="left:636px;top:74px">Our <span>Philosophy</span></h2>
  <div class="mark" style="left:636px;top:116px"><i></i></div>
  <div class="abs philo">
    <p class="para" style="left:20px;top:22px;width:383px">As web developers, we understand that a powerful and functional web site is a vital component of modern day marketing for companies of today. This is why our web site development team work with all of our clients to ensure their web site design will deliver to their target market.</p>
    <div class="btn" style="left:20px;top:162px"><i></i>Read More</div>
  </div>
</section>

<!-- Quick contact -->
<section class="band contact">
  <h2 class="abs h-title" style="left:0;width:1200px;text-align:center;top:71px">Quick <span>Contact</span></h2>
  <div class="mark" style="left:520px;top:112px"><b style="width:72px"></b><i></i><b style="width:72px"></b></div>
  <div class="field" style="left:302px;top:166px;width:289px;height:35px">First Name*</div>
  <div class="field" style="left:609px;top:166px;width:289px;height:35px">Last Name*</div>
  <div class="field" style="left:302px;top:217px;width:289px;height:37px">Email*</div>
  <div class="field robot" style="left:609px;top:217px;width:289px;height:37px"><i></i>I am not a robot<em></em></div>
  <div class="field" style="left:302px;top:273px;width:596px;height:86px">Message*</div>
  <div class="btn" style="left:550px;top:402px"><i></i>Submit</div>
</section>

<!-- Footer -->
<footer class="band footer">
  <div class="brand">plumvista•net</div>
  <p class="f-text" style="left:141px;top:113px;width:215px">Plumvista.net is an Australian based Software and Web Development Company that provides individual technology solutions and professional software for clients worldwide.</p>

  <div class="f-head" style="left:410px">Contact <span>Details</span></div>
  <ul class="f-list" style="left:410px">
    <li><svg width="12" height="12" viewBox="0 0 24 24" fill="#e3323b"><path d="M5 2h4l2 6-3 2a12 12 0 0 0 6 6l2-3 6 2v4a3 3 0 0 1-3 3A18 18 0 0 1 2 5a3 3 0 0 1 3-3z"/></svg>+61 7 5550 1234</li>
    <li><svg width="12" height="12" viewBox="0 0 24 24" fill="none" stroke="#e3323b" stroke-width="3"><rect x="6" y="2" width="12" height="20" rx="2"/></svg>+61 0400 555 018</li>
    <li><svg width="12" height="10" viewBox="0 0 24 18" fill="#e3323b"><path d="M0 0h24v18H0z"/><path d="M1 1l11 8 11-8" stroke="#2b2b2b" stroke-width="2" fill="none"/></svg>info@plumvista.com</li>
  </ul>

  <div class="f-head" style="left:633px">Quick <span>Links</span></div>
  <ul class="f-list f-links" style="left:633px">
    <li>Home</li><li>Our Services</li><li>Our Clients</li><li>Contact Us</li>
  </ul>

  <div class="f-head" style="left:776px">Subcribe <span>to your Newletter</span></div>
  <p class="f-text" style="left:776px;top:112px">You can be always up to date with our company news</p>
  <div class="abs sub-form"><span>Enter your Email*</span><b>Submit</b></div>
  <div class="abs" style="left:784px;top:185px;display:flex;gap:8px" aria-label="Social links"><i class="social"></i><i class="social"></i><i class="social"></i></div>

  <div class="abs f-rule"></div>
  <div class="abs copy">© 2019 plumvista. All Right Reserved.</div>
</footer>

</body>
</html>
```